Web Design Project for lawn care business

after having a logo designed now my website is letting me down.
My websites main purpose is once i have made contact with a customer most will then try to research my company and the work i have done. Going to my unprofessional and untidy site will only put off potential customers. Also some customers will find my site online so must be able to grab their attention.

My site must be in keeping with my logo. Which is modern, sleek and classy. It needs to convey how professional we are and that the customer is getting a professional service.

My existing site will be replaced with the winning design.

Content wise and amount of pages will be similar to mine how ever more data will be inputted by myself.

so far prefer sites designed incorporating links in pictures or animated links to flick through pictures etc

breaks up the site and is more user friendly. 

also need to make sure colours are in keeping with logo or at least have similarities to keep it all uniform.

thanks

Industry/Entity Type

Lawn Care

Requirements
Nice to have
• in keeping font wise with my logo
same colours etc

```html
<!DOCTYPE html>
<html lang="en">
<head>
<meta charset="utf-8">
<title>Fairway Lawn Care</title>
<link rel="stylesheet" href="https://fonts.googleapis.com/css2?family=Cinzel:wght@400;700&family=Roboto:wght@400&family=Open+Sans:wght@400;700&display=swap">
<style>
:root{
  --black:#000;
  --lime:#9ed048;
  --lime-bright:#8cc63f;
  --leaf:#5f9a2c;
  --ink:#f2f2f2;
  --brown:#3b1c0b;
  --footer-top:#0c1606;
  --footer-bottom:#3f6e1c;
}
*{margin:0;padding:0;box-sizing:border-box}
html,body{width:852px;height:1200px;overflow:hidden;background:var(--black)}
.page{position:relative;width:852px;height:1200px;background:var(--black);color:var(--ink);font-family:"Open Sans",sans-serif}
.abs{position:absolute}

.contact{top:24px;font-family:"Roboto",sans-serif;font-size:16px;color:var(--lime);display:flex;align-items:center;gap:8px}
.contact svg{fill:var(--lime)}
.contact-email{left:437px}
.contact-phone{left:663px}

.brand{left:34px;top:50px;display:flex;align-items:center;gap:12px}
.brand-mark{width:58px;height:58px;border-radius:50%;background:var(--lime);flex:none}
.brand-name{font-family:"Cinzel",serif;font-size:26px;font-weight:400;color:var(--lime);line-height:1.1;width:200px}

.nav{left:328px;top:73px;font-family:"Cinzel",serif;font-size:11.5px;color:var(--ink)}
.nav a{color:inherit;text-decoration:none;position:absolute;white-space:nowrap}

.hero{left:58px;top:124px;width:542px;height:247px;background:radial-gradient(ellipse at 60% 40%,#b6e06a 0%,#6fae2c 40%,#2f6a12 100%);border:1px solid #6a9a3a}
.quote{left:50px;top:321px;width:321px;height:37px;background:var(--brown);font-family:"Cinzel",serif;font-size:18px;color:var(--ink);padding:6px 0 0 41px}
.dots{left:534px;top:353px;display:flex;gap:7px}
.dots span{width:8px;height:8px;border-radius:50%;background:#d8d8d8;opacity:.7}

.commit-title{left:615px;top:120px;font-family:"Cinzel",serif;font-weight:400;font-size:18.5px;color:var(--lime)}
.commit{left:619px;top:169px;list-style:none;font-family:"Roboto",sans-serif;font-size:13.5px;color:var(--ink)}
.commit li{display:flex;gap:2px;height:46.5px;align-items:flex-start}
.commit li::before{content:"";width:14px;height:14px;background:var(--leaf);margin-top:1px;flex:none}

.services{left:0;top:390px;width:852px;height:205px;background:linear-gradient(180deg,#527e25 0%,#2e4c14 35%,#0a1204 80%,#000 100%)}
.divider{top:392px;width:2px;height:200px;background:linear-gradient(180deg,#6b8a4d,#3a3a3a)}
.service{top:419px;width:180px;text-align:center;transform:translateX(-90px)}
.service-icon{width:66px;height:66px;border-radius:50%;background:var(--leaf);margin:0 auto;display:flex;align-items:center;justify-content:center}
.service-icon svg{fill:#fff}
.service-label{margin-top:12px;font-family:"Cinzel",serif;font-weight:700;font-size:15px;color:var(--lime);letter-spacing:.3px}

.why-title{left:122px;top:606px;font-family:"Cinzel",serif;font-weight:400;font-size:28px;color:var(--lime)}
.why-col{top:658px;font-size:10px;line-height:13px;color:var(--ink);letter-spacing:-.1px;z-index:2}
.why-col.left{left:63px;width:176px}
.why-col.right{left:250px;width:188px}

.mower-art{left:450px;top:670px;width:402px;height:305px;background:linear-gradient(180deg,#000 0%,#0b1405 55%,#4f8a20 100%)}

.footer{left:0;top:975px;width:852px;height:210px;background:linear-gradient(180deg,var(--footer-top) 0%,#1c300c 55%,var(--footer-bottom) 100%)}
.footer-heading{font-family:"Open Sans",sans-serif;font-weight:700;font-size:9.5px;color:var(--ink);top:1022px}
.tweets{left:63px;top:1046px;width:170px;font-size:10.5px;line-height:13px;color:var(--ink)}
.tweets p{margin-bottom:7px}
.tweets .handle{color:var(--lime)}
.tweets .time{font-size:8.5px;margin-bottom:14px}
.tweets .link{color:var(--lime);font-style:italic;font-size:10px}
.footer-brand{left:322px;top:1044px;display:flex;align-items:center;gap:10px}
.footer-brand .brand-mark{width:46px;height:46px}
.footer-brand .brand-name{font-size:21px;width:160px}
.gallery{left:620px;top:1046px;display:grid;grid-template-columns:repeat(3,46px);column-gap:16px;row-gap:16px}
.gallery div{width:46px;height:46px;border:2px solid #fff}
.g1{background:#6fa22e}.g2{background:#c9dca4}.g3{background:#5f8c22}
.g4{background:#3e7a18}.g5{background:#8ec04a}.g6{background:#4a6e30}

.copyright{left:0;top:1185px;width:852px;height:15px;background:var(--lime-bright);text-align:center;font-size:8.5px;line-height:15px;color:#1d2a0d;letter-spacing:.3px}
</style>
</head>
<body>
<div class="page">

  <div class="abs contact contact-email">
    <svg width="17" height="12" viewBox="0 0 17 12"><path d="M0 0h17v12H0z"/><path d="M1.5 1.5l7 5 7-5" fill="none" stroke="#000" stroke-width="1.4"/></svg>
    <span>info@fairwaylawns.net</span>
  </div>
  <div class="abs contact contact-phone">
    <svg width="16" height="16" viewBox="0 0 24 24"><path d="M6.6 10.8a15.1 15.1 0 0 0 6.6 6.6l2.2-2.2a1 1 0 0 1 1-.25 11.4 11.4 0 0 0 3.6.57 1 1 0 0 1 1 1V20a1 1 0 0 1-1 1A17 17 0 0 1 3 4a1 1 0 0 1 1-1h3.5a1 1 0 0 1 1 1c0 1.25.2 2.45.57 3.57a1 1 0 0 1-.25 1z"/></svg>
    <span>07700 900 412</span>
  </div>

  <div class="abs brand">
    <div class="brand-mark"></div>
    <div class="brand-name">Fairway<br>Lawn Care</div>
  </div>

  <nav class="abs nav">
    <a style="left:0">Home</a>
    <a style="left:52px">Our Services</a>
    <a style="left:147px">Contact Us</a>
    <a style="left:236px">Useful Links</a>
    <a style="left:330px">Lawncare Advice</a>
    <a style="left:452px">FAQ</a>
  </nav>

  <div class="abs hero" role="img" aria-label="Close-up photograph of fresh green grass blades"></div>
  <div class="abs quote">Get A Free Quote Today!</div>
  <div class="abs dots"><span></span><span></span><span></span><span></span></div>

  <h2 class="abs commit-title">Our Commitment</h2>
  <ul class="abs commit">
    <li>Fully Insured</li>
    <li>All Waste Removed</li>
    <li>Qualified Greenkeepers</li>
    <li>Reliable, Prompt &amp; Flexible</li>
    <li>Free No Obligation Quotes</li>
  </ul>

  <div class="abs services"></div>
  <div class="abs divider" style="left:57px"></div>
  <div class="abs divider" style="left:246px"></div>
  <div class="abs divider" style="left:420px"></div>
  <div class="abs divider" style="left:598px"></div>
  <div class="abs divider" style="left:793px"></div>

  <div class="abs service" style="left:151px">
    <div class="service-icon"><svg width="22" height="22" viewBox="0 0 22 22"><circle cx="8" cy="8" r="5"/><circle cx="14" cy="10" r="5"/><rect x="10" y="13" width="2" height="8"/></svg></div>
    <div class="service-label">Garden Services</div>
  </div>
  <div class="abs service" style="left:334px">
    <div class="service-icon"><svg width="22" height="22" viewBox="0 0 22 22"><path d="M11 1l3 5 5-1-2 5 4 3-6 1 1 4-5-3-5 3 1-4-6-1 4-3-2-5 5 1z"/><rect x="10" y="15" width="2" height="6"/></svg></div>
    <div class="service-label">Tree Services</div>
  </div>
  <div class="abs service" style="left:507px">
    <div class="service-icon"><svg width="22" height="24" viewBox="0 0 22 24"><path d="M11 23C9 16 4 13 2 6c5 3 8 8 9 17zM11 23c0-8 2-14 6-20 1 8-2 14-6 20zM11 23C11 15 8 9 10 1c3 7 3 14 1 22z"/></svg></div>
    <div class="service-label">Lawn Services</div>
  </div>
  <div class="abs service" style="left:697px">
    <div class="service-icon"><svg width="22" height="22" viewBox="0 0 22 22"><path d="M5 2h12v6a6 6 0 0 1-12 0zM2 3h3v2a3 3 0 0 0 1 2H4A3 3 0 0 1 2 4zM20 3h-3v2a3 3 0 0 1-1 2h2a3 3 0 0 0 2-3zM10 14h2v4h-2zM7 18h8v2H7z"/></svg></div>
    <div class="service-label">Sports Surface</div>
  </div>

  <h2 class="abs why-title">WHY CHOOSE US?</h2>

  <div class="abs mower-art" role="img" aria-label="Green silhouette illustration of a man pushing a lawn mower over grass"></div>

  <p class="abs why-col left">Just as the name suggests all work is carried out by fully qualified Greenkeepers. So why would you want to do it yourself? As Greenkeepers, the meticulous attention to detail and passion that goes into working on a golf course also goes into every <em>other</em> job we do from mowing to full hard landscaping jobs and everything in between. Everyone knows that golf greens are the most immaculate, well maintained and most aesthetically pleasing grassed areas on the planet. With this in mind who else would you want to have maintaining, renovating and constructing your own garden? That's where we come in.</p>
  <p class="abs why-col right">With access to every piece of equipment, material, chemical and staff needed to maintain a golf course, we are able to offer you the very same services tailored to your garden regardless how big or small and at an affordable price! Costing less than using DIY methods with inefficiant materials. Each staff member is fully qualified with a National Diploma in Sportsturf or above, a two year qualification in both practical work and theory. Our staff has a PA1, PA6 &amp; NPTC Spraying certificate which allow us to spray all the chemicals that most gardeners don't have access to. We also hold all relevant NPTC certificates in chainsaw for any arboriculture needs.</p>

  <footer class="abs footer"></footer>
  <h3 class="abs footer-heading" style="left:63px">TWITTER FEED</h3>
  <div class="abs tweets">
    <p>hey <span class="handle">@mossandmow</span> just got my design proofs back from Fernhill Studio Design, so excited!</p>
    <p class="time">1 day ago</p>
    <p style="margin-bottom:0">Just purchased <span class="handle">@fernhillstudio</span>'s awesome new ebook on owning a website, good read.</p>
    <p class="link">www.fernhillstudio.com</p>
  </div>

  <div class="abs footer-brand">
    <div class="brand-mark"></div>
    <div class="brand-name">Fairway<br>Lawn Care</div>
  </div>

  <h3 class="abs footer-heading" style="left:620px">GALLERY</h3>
  <div class="abs gallery">
    <div class="g1" role="img" aria-label="Photo of close-mown turf"></div>
    <div class="g2" role="img" aria-label="Photo of pale grass blades"></div>
    <div class="g3" role="img" aria-label="Photo of a lawn surface"></div>
    <div class="g4" role="img" aria-label="Photo of a single grass blade"></div>
    <div class="g5" role="img" aria-label="Photo of striped lawn pattern"></div>
    <div class="g6" role="img" aria-label="Photo of a mower on grass"></div>
  </div>

  <div class="abs copyright">COPYRIGHT©2013 FAIRWAY LAWN CARE, ALL RIGHTS RESERVED.</div>
</div>
</body>
</html>
```